menu tonavera

nesecitamos nuestro menu para restaurante mexicano lo qu ebuscamos es un menu moderno pero ala vez elegante de preferencia fondo negro o cafe y letras blancas o letras visibles con fotos

Target Market(s)

personas de todas edades

Industry/Entity Type

Mexican Restaurant

Font styles to use
Sans Serif

Colors
000000
fbfbfb
ec1f27
fbe7d2

Requirements
Must have
• elegancia, moderno presencia
Nice to have
• portada de menu logotipo con fondo moderno

```html
<!DOCTYPE html>
<html lang="en">
<head>
<meta charset="utf-8">
<title>Tonavera Menu</title>
<link rel="stylesheet" href="https://fonts.googleapis.com/css2?family=Cinzel:wght@400;700&family=Open+Sans:wght@400&display=swap">
<style>
:root{
  --page:#ffffff;
  --ink:#111111;
  --cream:#f6e2cf;
  --cream-deep:#e9c9a6;
  --charcoal:#2e2d2c;
  --charcoal-deep:#1d1c1b;
  --white:#fbfbfb;
  --brand:#8a4a2a;
  --photo-dark:#2a2420;
  --photo-warm:#c98e4c;
}
*{margin:0;padding:0;box-sizing:border-box}
html,body{width:1200px;height:1200px;overflow:hidden;background:var(--page)}
.menu{position:absolute;left:146px;top:12px;width:908px;height:1174px;font-family:"Cinzel",serif;color:var(--ink)}
.photo-top{position:absolute;left:0;top:0;width:908px;height:160px;background:linear-gradient(90deg,var(--photo-dark) 0%,#3a3430 25%,#d9d2c6 45%,#e8e2d8 60%,var(--photo-warm) 80%,#d8a868 100%)}
.photo-bottom{position:absolute;left:0;top:1056px;width:908px;height:118px;background:linear-gradient(90deg,#4a2f22 0%,#c7562e 20%,#d6b46a 45%,#a87b45 65%,#e0c080 85%,#6b4a30 100%)}
.brand-badge{position:absolute;left:42px;top:24px;width:112px;height:112px;border-radius:50%;background:#e6e3df;display:flex;align-items:center;justify-content:center;font-family:"Cinzel",serif;font-size:17px;color:var(--brand);letter-spacing:1px}
.cream-panel{position:absolute;left:0;top:160px;width:908px;height:500px;background:linear-gradient(100deg,var(--cream) 0%,#f1d8bf 45%,var(--cream-deep) 75%,#d9a878 100%)}
.rule-band{position:absolute;left:0;top:660px;width:908px;height:10px;background:#000}
.dark-panel{position:absolute;left:0;top:672px;width:908px;height:384px;background:linear-gradient(100deg,#3a3937 0%,var(--charcoal) 40%,var(--charcoal-deep) 100%)}
.edge-tab{position:absolute;width:8px;border-radius:8px;background:#1a1a1a}
.el{position:absolute;white-space:nowrap}
.heading{font-weight:700;font-size:29px}
.heading-lg{font-weight:700;font-size:32px}
.item{font-size:21px;letter-spacing:.3px}
.desc{font-size:11px;letter-spacing:.3px}
.price{font-family:"Cinzel",serif;font-size:19px}
.divider{position:absolute;left:452px;top:202px;width:1px;height:338px;background:#333}
.extras-box{position:absolute;left:130px;top:542px;width:650px;height:114px}
.extras-text{position:absolute;left:130px;width:650px;text-align:center;color:var(--white)}
.notice{font-family:"Open Sans",sans-serif;font-size:10px}
.light{color:var(--white)}
.fajitas-title{position:absolute;left:0;width:908px;text-align:center;top:696px;color:var(--white);font-size:29px}
.fajitas-line{position:absolute;left:263px;top:734px;width:381px;height:2px;background:linear-gradient(90deg,transparent,#e8e8e8 30%,#e8e8e8 70%,transparent)}
.small-note{font-size:10.5px}
</style>
</head>
<body>
<div class="menu">
  <div class="photo-top" role="img" aria-label="Plate of quesadilla wedges with guacamole, sour cream and salsa cups"></div>
  <div class="brand-badge">TONAVERA</div>

  <div class="cream-panel" role="img" aria-label="Soft warm background photo of a wooden table with food"></div>
  <div class="edge-tab" style="left:0;top:268px;height:286px"></div>
  <div class="edge-tab" style="right:0;top:256px;height:286px"></div>

  <section class="quesadillas">
    <h2 class="el heading" style="left:23px;top:206px">Quesadillas</h2>
    <div class="el item" style="left:23px;top:274px">Tonavera al pastor quesadilla</div>
    <div class="el price" style="left:390px;top:276px">$11.50</div>
    <div class="el desc" style="left:21px;top:302px">Special marinated pork, cheese and pineapple</div>
    <div class="el item" style="left:19px;top:329px">Cheese quesadilla</div>
    <div class="el price" style="left:391px;top:328px">$7.50</div>
    <div class="el item" style="left:22px;top:362px">Fajita quesadilla</div>
    <div class="el price" style="left:389px;top:362px">$11.99</div>
    <div class="el desc" style="left:21px;top:389px">Steak, chicken or shrimp</div>
    <div class="el item" style="left:22px;top:414px">Shredded Chicken quesadilla</div>
    <div class="el price" style="left:391px;top:414px">$9.00</div>
    <div class="el item" style="left:21px;top:450px">Ground beef quesadilla</div>
    <div class="el price" style="left:391px;top:450px">$9.00</div>
  </section>

  <div class="divider"></div>

  <section class="nachos">
    <h2 class="el heading-lg" style="left:463px;top:200px">NACHOS</h2>
    <div class="el item" style="left:461px;top:248px">Fiesta Nachos</div>
    <div class="el price" style="left:834px;top:250px">$9.75</div>
    <div class="el desc" style="left:461px;top:271px">Shredded chicken or ground beef, lettuce, tomatoes, beans,</div>
    <div class="el desc" style="left:461px;top:285px">cheese, sour cream, guacamole and jalapenos.</div>
    <div class="el item" style="left:461px;top:312px">Grill NAchos</div>
    <div class="el price" style="left:830px;top:305px">$11.75</div>
    <div class="el desc" style="left:461px;top:340px">Grilled steak or chicken, lettuce, beans, cheese, sour cream,</div>
    <div class="el desc" style="left:461px;top:354px">pico de gallo, guacamole and jalapenos.</div>
    <div class="el item" style="left:461px;top:376px">Nachos Shredded chicken</div>
    <div class="el price" style="left:834px;top:378px">$7.55</div>
    <div class="el desc" style="left:461px;top:400px">Cheese, beans, shredded chicken and jalapenos.</div>
    <div class="el item" style="left:461px;top:429px">Nachos Ground Beef</div>
    <div class="el price" style="left:834px;top:431px">$7.55</div>
    <div class="el desc" style="left:461px;top:453px">Cheese, beans, ground beef and jalapenos</div>
    <div class="el item" style="left:461px;top:482px">Cheese Nachos</div>
    <div class="el price" style="left:834px;top:488px">$6.50</div>
    <div class="el desc" style="left:461px;top:504px">cheese, beans and jalapenos.</div>
  </section>

  <svg class="extras-box" viewBox="0 0 650 114" aria-hidden="true">
    <path d="M32 0 H619 Q634 0 636 14 L650 114 H0 L14 14 Q17 0 32 0 Z" fill="#1b1b1b"/>
  </svg>
  <div class="extras-text" style="top:553px;font-size:12px">Each extra ingredient : $1.00</div>
  <div class="extras-text" style="top:575px;font-size:14.5px">Lettuce, chopped Tomatoes, pico de gallo, sour cream,</div>
  <div class="extras-text" style="top:593px;font-size:14.5px">shredded cheese, guacamole, jalapenos, green sauce or cheese dip.</div>
  <div class="extras-text notice" style="top:614px">Notice: May be cooked to order. Consuming raw or under cooked meats, poultry, seafood, shelfish or</div>
  <div class="extras-text notice" style="top:628px">eggs may increase your risk of foodborne illness, especially if you have certain medical conditions.</div>

  <div class="rule-band"></div>

  <div class="dark-panel" role="img" aria-label="Dark background photo of a sizzling fajita skillet"></div>
  <div class="edge-tab" style="left:0;top:788px;height:268px;background:#555"></div>
  <div class="edge-tab" style="right:0;top:788px;height:268px;background:#555"></div>

  <section class="fajitas light">
    <h2 class="fajitas-title">Fajitas</h2>
    <div class="fajitas-line"></div>
    <div class="el light" style="left:33px;top:754px;font-size:14px">All fajitas are cooked with tomatoes, bell peppers and onions, served with rice beans, lettuce,</div>
    <div class="el light" style="left:33px;top:772px;font-size:14px">soour cream, guacamole, pico degallo and an order of tortillas</div>

    <div class="el item light" style="left:20px;top:818px">Alambres Tonavera</div>
    <div class="el price light" style="left:386px;top:820px">$14.59</div>
    <div class="el small-note light" style="left:23px;top:845px">for one</div>
    <div class="el desc light" style="left:23px;top:864px">steak, chicken and becon with onions, bell pepper,</div>
    <div class="el desc light" style="left:23px;top:878px">tomatoes and melted mozzarella cheese</div>

    <div class="el item light" style="left:20px;top:898px">Steak, Chicken or Combo</div>
    <div class="el price light" style="left:384px;top:900px">$13.99</div>
    <div class="el small-note light" style="left:23px;top:920px">for one</div>

    <div class="el item light" style="left:20px;top:950px">Shrimp Fajitas</div>
    <div class="el price light" style="left:384px;top:951px">$14.99</div>
    <div class="el small-note light" style="left:23px;top:975px">for one</div>

    <div class="el item light" style="left:20px;top:1004px">Vegetable Fajita</div>
    <div class="el price light" style="left:384px;top:1005px">$10.59</div>

    <div class="el item light" style="left:463px;top:816px">Fajita Azteca</div>
    <div class="el price light" style="left:828px;top:818px">$15.99</div>
    <div class="el small-note light" style="left:466px;top:843px">for one</div>
    <div class="el desc light" style="left:466px;top:862px">steak, chicken shrimp, becon and pireapple</div>

    <div class="el item light" style="left:463px;top:898px">Fajita Mexicana</div>
    <div class="el price light" style="left:826px;top:900px">$15.99</div>
    <div class="el small-note light" style="left:466px;top:919px">for one</div>
    <div class="el desc light" style="left:466px;top:933px">steak, chicken shrimp and Mexican sausage.</div>

    <div class="el item light" style="left:463px;top:973px">Texas Fajitas</div>
    <div class="el price light" style="left:826px;top:975px">$14.99</div>
    <div class="el small-note light" style="left:466px;top:997px">for one</div>
    <div class="el desc light" style="left:466px;top:1011px">steak, chicken and shrimp.</div>
  </section>

  <div class="photo-bottom" role="img" aria-label="Close-up of grilled chicken fajitas with peppers and onions"></div>
</div>
</body>
</html>
```